CASH PAYMENT DISCOUNT NOTICE POSTED IN CASH REGISTER AREA

LOOKING TO MAKE A FLYER OR A POSTED NOTICE FOR CUSTOMERS PAYING FOR OVER-THE-COUNTER MERCHANDISE AND WHO PAY BY CASH METHOD TO GET A 4% CASH DISCOUNT.
PRESCRIPTIONS ARE EXCLUDED FROM THIS CASH DISCOUNT.

Target Market(s)

RETAIL CUSTOMERS

Industry/Entity Type

RETAIL PHARMACY

Colors
0054AA
0677BA
7BADD7
CADEEF
E8F1F8
EB3D1F
EC4F4E
F09395
F8D3D4
FCEDEE

Requirements
Must have
• LOGO COLORS
Nice to have
• EYE CATCHING

```html
<!DOCTYPE html>
<html lang="en">
<head>
<meta charset="utf-8">
<title>Cash Discount Notice</title>
<link rel="stylesheet" href="https://fonts.googleapis.com/css2?family=Montserrat:wght@700;800&display=swap">
<style>
  :root {
    --backdrop: #e4e4e4;
    --brand-blue: #354a9a;
    --accent-red: #c0161e;
    --paper: #ffffff;
    --ink: #1a1a1a;
  }
  html, body {
    margin: 0;
    padding: 0;
    width: 1200px;
    height: 1200px;
    overflow: hidden;
    background: var(--backdrop);
    font-family: "Montserrat", Arial, sans-serif;
  }
  .notice {
    position: absolute;
    left: 67px;
    top: 286px;
    width: 1066px;
    height: 614px;
    background: var(--brand-blue);
    box-sizing: border-box;
  }
  .notice__brand {
    position: absolute;
    left: 9px;
    top: 9px;
    right: 9px;
    height: 252px;
    background: var(--paper);
    display: flex;
    align-items: center;
    justify-content: center;
    gap: 22px;
  }
  .brand-mark {
    width: 54px;
    height: 54px;
    background: var(--brand-blue);
  }
  .brand-name {
    color: var(--brand-blue);
    font-weight: 800;
    font-size: 52px;
    letter-spacing: 2px;
    line-height: 1;
  }
  .notice__title {
    position: absolute;
    left: 0;
    right: 0;
    top: 261px;
    height: 83px;
    margin: 0;
    color: var(--paper);
    font-weight: 800;
    font-size: 70px;
    line-height: 83px;
    text-align: center;
    letter-spacing: 1px;
  }
  .notice__body {
    position: absolute;
    left: 9px;
    right: 9px;
    top: 344px;
    height: 208px;
    background: var(--paper);
    display: flex;
    align-items: center;
    justify-content: center;
  }
  .notice__message {
    margin: 0;
    color: var(--ink);
    font-weight: 700;
    font-size: 29px;
    line-height: 41px;
    text-align: center;
    letter-spacing: 0.5px;
  }
  .notice__highlight {
    color: var(--accent-red);
  }
  .notice__exclusion {
    position: absolute;
    left: 0;
    right: 0;
    bottom: 0;
    height: 62px;
    margin: 0;
    color: var(--paper);
    font-weight: 700;
    font-size: 22px;
    line-height: 62px;
    text-align: center;
    letter-spacing: 0.6px;
  }
</style>
</head>
<body>
  <section class="notice">
    <header class="notice__brand">
      <span class="brand-mark" aria-hidden="true"></span>
      <span class="brand-name">MERIDIAN PHARMACY</span>
    </header>
    <h1 class="notice__title">CASH DISCOUNT</h1>
    <div class="notice__body">
      <p class="notice__message">
        AS AN INCENTIVE FOR CUSTOMERS, WE NOW<br>
        PROVIDE A DISCOUNT TO PAY WITH CASH BY GIVING<br>
        A <span class="notice__highlight">4% IMMEDIATE DISCOUNT</span> ON THE SERVICE CHARGE.
      </p>
    </div>
    <p class="notice__exclusion">PRESCRIPTIONS ARE EXCLUDED FROM THIS CASH DISCOUNT</p>
  </section>
</body>
</html>
```